Elmcrest Tutoring & Test Preparation
stationery and business card
Elmcrest Tutoring & Test Preparation - Education
Creative Brief
Simple
Doreen Falk
Director
Elmcrest Tutoring & Test Prep 245 Marlowe Park Rd, 3-B Larkfield, NJ 08561
dfalk@elmcresttutors.com
www.elmcresttutors.com
Elmcrest is a premier tutoring and test prep firm, and we focus on grades 7 - 12, college counseling
a quick list of tutoring services -- "ACT, SAT/PSAT, SSAT, SAT Subject Tests, Academic Tutoring, Reading and Study Skills, College Counseling"

```html
<!DOCTYPE html>
<html lang="en">
<head>
<meta charset="utf-8">
<title>Elmcrest Tutoring &amp; Test Prep – Business Card</title>
<link href="https://fonts.googleapis.com/css2?family=Crimson+Text:wght@400;700&display=swap" rel="stylesheet">
<style>
  :root {
    --page: #e9ebee;
    --card: #ffffff;
    --card-shade: #eef0f3;
    --brand: #1d4fa8;
    --brand-light: #4f86d8;
    --brand-deep: #162c6b;
    --ink: #2a2f3a;
    --muted: #6b7280;
  }
  * { box-sizing: border-box; margin: 0; padding: 0; }
  html, body { width: 1200px; height: 901px; overflow: hidden; }
  body {
    background: var(--page);
    font-family: "Crimson Text", Georgia, serif;
    color: var(--ink);
    position: relative;
  }
  .card {
    position: absolute;
    width: 540px;
    height: 309px;
    background: linear-gradient(135deg, var(--card) 55%, var(--card-shade));
    box-shadow: 0 10px 30px rgba(20, 30, 50, .18);
    overflow: hidden;
  }
  .card--back { left: 40px; top: 296px; }
  .card--front { left: 620px; top: 296px; }

  /* back side */
  .back-mark {
    position: absolute; left: 150px; top: 70px;
    width: 130px; height: 130px; border-radius: 50%;
    background: radial-gradient(circle at 35% 30%, var(--brand-light), var(--brand) 55%, var(--brand-deep));
  }
  .back-name {
    position: absolute; left: 296px; top: 112px;
    font-size: 30px; color: var(--brand-deep); letter-spacing: 1px;
  }
  .services {
    position: absolute; left: 70px; top: 222px; width: 400px;
    text-align: center; font-size: 13.5px; line-height: 1.45; color: var(--brand);
  }

  /* front side */
  .brand {
    position: absolute; left: 30px; top: 36px;
    display: flex; align-items: center; gap: 12px;
  }
  .brand-mark {
    width: 50px; height: 50px; border-radius: 50%;
    background: radial-gradient(circle at 35% 30%, var(--brand-light), var(--brand) 55%, var(--brand-deep));
  }
  .brand-name { font-size: 22px; color: var(--brand-deep); line-height: 1.05; }
  .brand-name span { display: block; font-size: 12px; letter-spacing: 2px; text-transform: uppercase; }

  .address {
    position: absolute; left: 34px; top: 118px;
    font-size: 14px; line-height: 1.3; font-style: normal;
  }
  .contacts {
    position: absolute; left: 34px; top: 196px;
    list-style: none; font-size: 14px; line-height: 1.6;
  }
  .contacts li { display: flex; align-items: center; gap: 8px; }
  .contacts svg { width: 14px; height: 14px; fill: var(--brand-deep); flex: none; }

  .person {
    position: absolute; right: 44px; top: 128px; text-align: center;
  }
  .person-name { font-size: 19px; font-weight: 700; color: var(--brand-deep); }
  .person-title { font-size: 13px; color: var(--muted); }

  .edge-band {
    position: absolute; left: 0; bottom: 40px; width: 8px; height: 80px;
    background: linear-gradient(var(--brand), var(--brand-deep));
  }
</style>
</head>
<body>
  <section class="card card--back" aria-label="Business card, back">
    <div class="back-mark"></div>
    <div class="back-name">Elmcrest</div>
    <p class="services">ACT, SAT/PSAT, SSAT, SAT Subject Tests, Academic Tutoring,<br>Reading and Study Skills, College Counseling</p>
  </section>

  <section class="card card--front" aria-label="Business card, front">
    <div class="brand">
      <div class="brand-mark"></div>
      <div class="brand-name">Elmcrest <span>Tutoring and Test Prep</span></div>
    </div>

    <address class="address">
      Elmcrest Tutoring &amp; Test Prep<br>
      245 Marlowe Park Rd, 3-B<br>
      Larkfield, NJ 08561
    </address>

    <ul class="contacts">
      <li><svg viewBox="0 0 16 16"><path d="M3 1h3l1 4-2 1a9 9 0 0 0 5 5l1-2 4 1v3c0 1-1 2-2 2A13 13 0 0 1 1 3c0-1 1-2 2-2z"/></svg>609-555-0142</li>
      <li><svg viewBox="0 0 16 16"><path d="M5 0h6a1 1 0 0 1 1 1v14a1 1 0 0 1-1 1H5a1 1 0 0 1-1-1V1a1 1 0 0 1 1-1zm0 2v10h6V2z"/></svg>609-555-0187</li>
      <li><svg viewBox="0 0 16 16"><path d="M1 3h14v10H1zm1 1v1l6 4 6-4V4z"/></svg>dfalk@elmcresttutors.com</li>
    </ul>

    <div class="person">
      <div class="person-name">Doreen Falk</div>
      <div class="person-title">Director</div>
    </div>

    <div class="edge-band"></div>
  </section>
</body>
</html>
```